Dryer Vent Cleaning Postcard Design

We need a postcard design for Flue Wranglers, a company that specializes in dryer vent cleaning, repairs and upgrades. Dryer vents need periodic cleaning to avoid lint clogging, dryer malfunction, long dry times and even a house fire. This card will be sent to residential and businesses prospects to introduce them to our services and the importance of maintaining their dryer vents. Our website is @ fluewrangling.com and provides information about our services, photos of our work and our general color scheme (purple/orange). Final print size will be 5x7 horizontal.

Target Market(s)

homeowners and business owners (spas, salons, grooming, gyms, laundrymats, etc)

Requirements
Must have
• Reduce the risk of fire
shortened dry times
lower energy consumption
18000 dryer fires caused in the US per year
Nice to have
• Does your dryer take too long to dry?

```html
<!DOCTYPE html>
<html lang="en">
<head>
<meta charset="utf-8">
<title>Flue Wranglers – Dryer Vent Cleaning Postcard</title>
<link href="https://fonts.googleapis.com/css2?family=Roboto:wght@300;400;500;700;900&display=swap" rel="stylesheet">
<style>
  :root{
    --purple:#3b2a6b;
    --purple-deep:#2d1f58;
    --orange:#e8552f;
    --orange-bright:#f0642e;
    --blue-soft:#8ea3dd;
    --peach:#f6dccb;
    --white:#ffffff;
    --ink:#1f1f2b;
    --bg:#ece8e4;
  }
  *{box-sizing:border-box;margin:0;padding:0}
  html,body{width:1200px;height:1200px;overflow:hidden;background:var(--bg);font-family:"Roboto",sans-serif}
  .card{position:absolute;left:230px;width:740px;height:526px;background:var(--white);overflow:hidden;box-shadow:0 6px 18px rgba(0,0,0,.18)}
  .card--front{top:44px}
  .card--back{top:626px}
  .abs{position:absolute}
  .shape-layer{position:absolute;inset:0;width:100%;height:100%}

  /* front */
  .hero-photo{left:0;top:0;width:740px;height:526px;background:linear-gradient(120deg,#f3c4b3 0%,#f5e3d6 40%,#e8d8cc 70%,#cbb9ae 100%)}
  .brand{left:28px;top:70px;display:flex;align-items:center;gap:8px}
  .brand__dot{width:22px;height:22px;border-radius:50%;background:var(--orange)}
  .brand__name{font-weight:700;font-size:19px;color:var(--purple)}
  .title-dryer{right:36px;top:14px;font-weight:900;font-size:66px;line-height:1;color:var(--orange-bright);letter-spacing:1px}
  .title-vent{right:30px;top:82px;font-weight:900;font-size:82px;line-height:1;color:var(--white)}
  .title-cleaning{right:40px;top:168px;font-weight:900;font-size:44px;line-height:1;color:var(--purple)}
  .illus{border-radius:6px}
  .illus--tech-brush{left:18px;top:180px;width:170px;height:216px;background:linear-gradient(180deg,#c9a488,#8f7360)}
  .illus--tech-vacuum{left:412px;top:276px;width:98px;height:222px;background:linear-gradient(180deg,#c9a488,#b33b2a)}
  .stat{left:510px;top:260px;width:194px;height:198px;background:var(--orange);border-radius:12px;color:var(--white);text-align:center;padding-top:12px}
  .stat__big{font-weight:900;font-size:48px;line-height:.92}
  .stat__small{font-weight:500;font-size:16px;line-height:1.2;margin-top:8px}
  .benefit{width:84px;height:84px;border-radius:50%;background:var(--orange);border:3px solid var(--white);color:var(--white);text-align:center;font-size:11px;font-weight:300;line-height:1.25;padding-top:10px}
  .benefit svg{display:block;margin:0 auto 4px}
  .benefit--energy{font-size:10.5px}
  .benefit--fire{left:144px;top:276px}
  .benefit--dry{left:231px;top:308px}
  .benefit--energy{left:320px;top:342px}
  .callbox{left:28px;top:452px;width:178px;height:42px;border:2px solid var(--orange);border-radius:6px;text-align:center}
  .callbox__label{position:absolute;top:-11px;left:50%;transform:translateX(-50%);background:var(--white);padding:0 5px;color:var(--orange);font-size:13px;font-weight:500;white-space:nowrap}
  .callbox__phone{font-size:24px;color:var(--ink);line-height:40px}
  .contact{font-size:12px;color:var(--ink);display:flex;align-items:center;gap:6px}
  .contact--email{left:224px;top:456px}
  .contact--web{left:224px;top:474px}

  /* back */
  .services-tab{left:0;top:29px;width:154px;height:36px;background:var(--orange);border-radius:0 18px 18px 0;color:var(--white);font-weight:500;font-size:26px;line-height:36px;padding-left:38px}
  .service-list{left:38px;top:80px;list-style:none;color:var(--white);font-size:12.5px;font-weight:300}
  .service-list li{display:flex;align-items:center;gap:6px;height:35px}
  .tick{width:14px;height:14px;border-radius:50%;background:var(--orange);display:flex;align-items:center;justify-content:center}
  .proof{width:78px;height:78px;border-radius:50%;border:2px solid var(--orange);overflow:hidden}
  .proof__label{position:absolute;top:0;left:0;width:100%;height:20px;background:var(--orange);color:var(--white);font-size:11px;font-weight:700;text-align:center;line-height:18px}
  .proof__photo{width:100%;height:100%;background:radial-gradient(circle at 50% 55%,#111 0%,#3a3a3a 45%,#8a8a8a 100%)}
  .proof__photo--duct{background:linear-gradient(180deg,#6b6b6b,#3d3d3d 60%,#222)}
  .action-band{left:0;top:312px;width:400px;height:76px;background:var(--orange)}
  .action{width:110px;text-align:center;color:var(--white);font-size:12.5px;font-weight:300;line-height:1.2}
  .action__icon{width:64px;height:64px;margin:0 auto 6px;border-radius:50%;background:var(--white);border:3px solid var(--orange);box-shadow:0 0 0 2px var(--white);display:flex;align-items:center;justify-content:center}
  .action--clean{left:9px;top:274px}
  .action--online{left:114px;top:274px}
  .action--repair{left:223px;top:274px}
  .cta-title{left:28px;top:402px;font-size:36px;font-weight:500;color:var(--orange-bright)}
  .cta-phone{left:28px;top:440px;font-size:36px;font-weight:700;color:var(--white)}
  .back-contact{font-size:11px;color:var(--white);display:flex;align-items:center;gap:5px;top:486px;white-space:nowrap}
  .back-contact--email{left:28px}
  .back-contact--web{left:186px}
  .illus--tech-back{left:350px;top:290px;width:140px;height:222px;background:linear-gradient(180deg,#c9a488,#8f7360 70%,#5a4a8a)}
  .mini-brand{left:464px;top:70px;display:flex;align-items:center;gap:5px}
  .mini-brand__dot{width:12px;height:12px;border-radius:50%;background:var(--orange)}
  .mini-brand__name{font-size:11px;font-weight:700;color:var(--purple)}
  .stamp{left:648px;top:51px;width:48px;height:56px;background:#dedede}
  .address-line{left:500px;width:196px;height:1px;background:#d4d4d4}
</style>
</head>
<body>

<section class="card card--front" aria-label="Postcard front">
  <div class="abs hero-photo" role="img" aria-label="Photo of a worker on a rooftop cleaning a vent"></div>
  <svg class="shape-layer" viewBox="0 0 740 526" aria-hidden="true">
    <path d="M0 292 Q120 270 260 330 Q480 430 740 470 L740 526 L0 526Z" fill="var(--purple)"/>
    <path d="M0 446 Q210 350 420 420 Q600 480 740 520 L740 526 L0 526Z" fill="var(--white)"/>
    <path d="M420 500 Q600 470 740 380 L740 412 Q610 490 420 510Z" fill="var(--blue-soft)"/>
    <path d="M440 122 L464 85 L712 85 L712 161 L464 161Z" fill="var(--purple)"/>
  </svg>

  <div class="abs brand">
    <span class="brand__dot"></span><span class="brand__name">Flue Wranglers</span>
  </div>

  <div class="abs title-dryer">DRYER</div>
  <div class="abs title-vent">VENT</div>
  <div class="abs title-cleaning">CLEANING</div>

  <div class="abs illus illus--tech-brush" role="img" aria-label="Illustration of a technician holding a vent brush"></div>
  <div class="abs illus illus--tech-vacuum" role="img" aria-label="Illustration of a technician pushing a red vent vacuum"></div>

  <div class="abs stat">
    <div class="stat__big">18000<br>DRYER<br>FIRES</div>
    <div class="stat__small">CAUSED IN THE US<br>PER YEAR</div>
  </div>

  <div class="abs benefit benefit--fire">
    <svg width="22" height="24" viewBox="0 0 22 24"><path d="M11 1 C14 6 18 8 17 14 C16 19 13 20 11 20 C8 20 5 18 5 14 C5 10 8 9 8 5 C10 7 10 9 11 10 C12 7 12 4 11 1Z" fill="none" stroke="#fff" stroke-width="1.6"/><path d="M5 23 H17" stroke="#fff" stroke-width="1.6"/></svg>
    Reduce the<br>risk of fire
  </div>
  <div class="abs benefit benefit--dry">
    <svg width="22" height="22" viewBox="0 0 22 22"><rect x="2" y="4" width="18" height="16" rx="2" fill="none" stroke="#fff" stroke-width="1.6"/><path d="M2 8 H20 M6 1 V6 M16 1 V6 M8 11 L14 17 M14 11 L8 17" stroke="#fff" stroke-width="1.6"/></svg>
    shortened<br>dry times
  </div>
  <div class="abs benefit benefit--energy">
    <svg width="24" height="22" viewBox="0 0 24 22"><path d="M3 20 V16 M7 20 V13 M11 20 V10 M15 20 V7 M19 20 V4" stroke="#fff" stroke-width="2"/><circle cx="5" cy="5" r="3" fill="none" stroke="#fff" stroke-width="1.2"/></svg>
    lower energy<br>consumption
  </div>

  <div class="abs callbox">
    <span class="callbox__label">• Call Us Now ! •</span>
    <div class="callbox__phone">555-014-2290</div>
  </div>
  <div class="abs contact contact--email">
    <svg width="13" height="9" viewBox="0 0 13 9"><rect width="13" height="9" fill="var(--orange)"/><path d="M0 0 L6.5 5 L13 0" fill="none" stroke="#fff"/></svg>
    office@fluewrangling.com
  </div>
  <div class="abs contact contact--web">
    <svg width="12" height="12" viewBox="0 0 12 12"><circle cx="6" cy="6" r="5" fill="none" stroke="var(--orange)" stroke-width="1.3"/><path d="M1 6 H11 M6 1 Q3 6 6 11 Q9 6 6 1" fill="none" stroke="var(--orange)" stroke-width="1"/></svg>
    www.fluewrangling.com
  </div>
</section>

<section class="card card--back" aria-label="Postcard back">
  <svg class="shape-layer" viewBox="0 0 740 526" aria-hidden="true">
    <path d="M0 0 L400 0 Q470 70 440 170 Q400 300 350 390 Q320 460 350 526 L0 526Z" fill="var(--blue-soft)"/>
    <path d="M0 0 L364 0 Q440 80 410 180 Q370 300 320 400 Q300 460 330 526 L0 526Z" fill="var(--purple)"/>
    <rect x="0" y="514" width="350" height="12" fill="var(--blue-soft)"/>
  </svg>

  <div class="abs services-tab">Services</div>
  <ul class="abs service-list">
    <li><span class="tick"><svg width="8" height="8" viewBox="0 0 8 8"><path d="M1 4 L3 6 L7 1.5" fill="none" stroke="#fff" stroke-width="1.5"/></svg></span>Dryer Vent Cleaning</li>
    <li><span class="tick"><svg width="8" height="8" viewBox="0 0 8 8"><path d="M1 4 L3 6 L7 1.5" fill="none" stroke="#fff" stroke-width="1.5"/></svg></span>Dryer Vent Repair &amp; Installation</li>
    <li><span class="tick"><svg width="8" height="8" viewBox="0 0 8 8"><path d="M1 4 L3 6 L7 1.5" fill="none" stroke="#fff" stroke-width="1.5"/></svg></span>Transition Vent Replacement</li>
    <li><span class="tick"><svg width="8" height="8" viewBox="0 0 8 8"><path d="M1 4 L3 6 L7 1.5" fill="none" stroke="#fff" stroke-width="1.5"/></svg></span>Vent Cap Replacement</li>
    <li><span class="tick"><svg width="8" height="8" viewBox="0 0 8 8"><path d="M1 4 L3 6 L7 1.5" fill="none" stroke="#fff" stroke-width="1.5"/></svg></span>Bird / Rodent Guard</li>
  </ul>

  <div class="abs proof" style="left:238px;top:54px"><div class="proof__photo" role="img" aria-label="Photo of a lint-clogged vent duct before cleaning"></div><span class="proof__label">Before</span></div>
  <div class="abs proof" style="left:314px;top:54px"><div class="proof__photo" role="img" aria-label="Photo of a clean vent duct after cleaning"></div><span class="proof__label">After</span></div>
  <div class="abs proof" style="left:238px;top:158px"><div class="proof__photo proof__photo--duct" role="img" aria-label="Photo of a crushed transition duct before repair"></div><span class="proof__label">Before</span></div>
  <div class="abs proof" style="left:314px;top:158px"><div class="proof__photo proof__photo--duct" role="img" aria-label="Photo of a new transition duct after repair"></div><span class="proof__label">After</span></div>

  <div class="abs action-band"></div>
  <div class="abs illus illus--tech-back" role="img" aria-label="Illustration of a technician with a vent brush and rotary hose"></div>

  <div class="abs action action--clean">
    <div class="action__icon"><svg width="30" height="24" viewBox="0 0 30 24"><path d="M2 4 H18 V18 H2Z M18 9 H24 L28 14 V18 H18Z" fill="var(--orange)"/><circle cx="8" cy="19" r="3" fill="var(--orange)" stroke="#fff" stroke-width="1.5"/><circle cx="23" cy="19" r="3" fill="var(--orange)" stroke="#fff" stroke-width="1.5"/></svg></div>
    Dryer Vent<br>Cleaning
  </div>
  <div class="abs action action--online">
    <div class="action__icon"><svg width="30" height="26" viewBox="0 0 30 26"><ellipse cx="12" cy="10" rx="10" ry="8" fill="var(--orange)"/><path d="M6 16 L4 22 L11 17Z" fill="var(--orange)"/><ellipse cx="20" cy="14" rx="8" ry="6.5" fill="none" stroke="var(--orange)" stroke-width="2"/></svg></div>
    Schedule<br>Online
  </div>
  <div class="abs action action--repair">
    <div class="action__icon"><svg width="28" height="28" viewBox="0 0 28 28"><path d="M4 24 L15 13" stroke="var(--orange)" stroke-width="5" stroke-linecap="round"/><path d="M15 13 A7 7 0 1 1 22 6 L18 8 L20 10 L24 8 A7 7 0 0 1 15 13Z" fill="var(--orange)"/></svg></div>
    Dryer Vent<br>Repairs
  </div>

  <div class="abs cta-title">Call Now!</div>
  <div class="abs cta-phone">555-014-2290</div>
  <div class="abs back-contact back-contact--email">
    <svg width="13" height="9" viewBox="0 0 13 9"><rect width="13" height="9" fill="var(--orange)"/><path d="M0 0 L6.5 5 L13 0" fill="none" stroke="#fff"/></svg>
    office@fluewrangling.com
  </div>
  <div class="abs back-contact back-contact--web">
    <svg width="12" height="12" viewBox="0 0 12 12"><circle cx="6" cy="6" r="5" fill="none" stroke="var(--orange)" stroke-width="1.3"/><path d="M1 6 H11 M6 1 Q3 6 6 11 Q9 6 6 1" fill="none" stroke="var(--orange)" stroke-width="1"/></svg>
    www.fluewrangling.com
  </div>

  <div class="abs mini-brand"><span class="mini-brand__dot"></span><span class="mini-brand__name">Flue Wranglers</span></div>
  <div class="abs stamp"></div>
  <div class="abs address-line" style="top:206px"></div>
  <div class="abs address-line" style="top:280px"></div>
  <div class="abs address-line" style="top:358px"></div>
  <div class="abs address-line" style="top:437px"></div>
</section>

</body>
</html>
```